American cannabis tech company business card design

Thrum.com is seeking a modern, professional, and brand-aligned business card that represents our company and its core values: Mission, Story, Values, and Impact. As an innovative cannabis company, we want a business card that is not only visually appealing but also serves as a representation of who we are and what we stand for.

Project Scope: Design a double-sided business card that integrates our brand identity and core values. Incorporate our key brand elements, ensuring a sleek and contemporary aesthetic. Visually reflect our core values (Mission, Story, Values, Impact) in a way that is engaging yet professional.

Target Market(s)

Vendors, third parties,

Contact Information for Business Card

Contact details (name, title, email, phone, website, etc.)

Font styles to use
Other font styles liked:
• Caslon, Centra

Colors

Designer to choose colors to be used in the design.

Requirements
Must have
• Thrum.com logo and branding A creative yet clean way to integrate our core values (Mission, Story, Values, Impact) Modern typography and a well-structured layout
Nice to have
• forest green, grey, white, black
Should not have
• references to marijuana, leafs, plants, or related product

```html
<!DOCTYPE html>
<html lang="en">
<head>
<meta charset="utf-8">
<title>Thrum.com Business Card</title>
<link href="https://fonts.googleapis.com/css2?family=Poppins:wght@400;600;800&display=swap" rel="stylesheet">
<style>
  :root {
    --forest: #17331a;
    --page: #e9e6e4;
    --frost-light: #f4f2f1;
    --frost-mid: #dcd6d4;
    --white: #ffffff;
  }
  html, body {
    margin: 0;
    padding: 0;
    width: 1200px;
    height: 900px;
    overflow: hidden;
    background: var(--page);
  }
  .business-card {
    position: absolute;
    left: 100px;
    top: 142px;
    width: 1000px;
    height: 616px;
    box-shadow: 0 14px 40px rgba(0, 0, 0, 0.18);
  }
  .business-card svg { display: block; }
  .card-text { font-family: "Poppins", sans-serif; }
  .holder-name { font-weight: 600; font-size: 40px; fill: var(--white); letter-spacing: 0.5px; }
  .holder-title { font-weight: 400; font-size: 28px; fill: var(--white); }
  .contact-line { font-weight: 400; font-size: 29px; fill: var(--white); }
  .brand-name { font-weight: 800; font-size: 128px; fill: var(--forest); letter-spacing: -2px; }
  .contact-icon { fill: none; stroke: var(--white); stroke-width: 2.4; }
  .contact-icon-solid { fill: var(--white); }
</style>
</head>
<body>
  <div class="business-card">
    <svg width="1000" height="616" viewBox="0 0 1000 616" xmlns="http://www.w3.org/2000/svg">
      <defs>
        <linearGradient id="frost" x1="0" y1="0" x2="1" y2="0.3">
          <stop offset="0" stop-color="var(--frost-mid)"/>
          <stop offset="0.5" stop-color="var(--frost-light)"/>
          <stop offset="1" stop-color="#ebe6e5"/>
        </linearGradient>
      </defs>

      <rect class="card-base" width="1000" height="616" fill="var(--forest)"/>
      <polygon class="accent-wedge" points="5,275 1000,63 1000,535" fill="url(#frost)"/>

      <text class="card-text holder-name" x="41" y="130">DANIEL HAYES</text>
      <text class="card-text holder-title" x="41" y="166">Managing Director</text>

      <text class="card-text brand-name" x="934" y="340" text-anchor="end">THRUM</text>

      <!-- contact list -->
      <g class="contact-phone">
        <path class="contact-icon" d="M46 425c-4 4 2 14 9 19s12 6 15 3l2-3-5-5-4 3c-3-1-8-6-9-9l3-4-5-5z"/>
        <path class="contact-icon" d="M60 422a10 10 0 0 1 9 9M60 417a15 15 0 0 1 14 14"/>
        <text class="card-text contact-line" x="79" y="445">044-987 654 321</text>
      </g>
      <g class="contact-email">
        <rect class="contact-icon" x="45" y="465" width="26" height="17"/>
        <path class="contact-icon" d="M45 465l13 10 13-10"/>
        <text class="card-text contact-line" x="79" y="481">hello@thrumcard.com</text>
      </g>
      <g class="contact-web">
        <circle class="contact-icon" cx="58" cy="510" r="12"/>
        <ellipse class="contact-icon" cx="58" cy="510" rx="5" ry="12"/>
        <path class="contact-icon" d="M46 510h24M48 504h20M48 516h20"/>
        <text class="card-text contact-line" x="79" y="518">www.thrumcard.com</text>
      </g>
    </svg>
  </div>
</body>
</html>
```